Letterhead and Envelope Design for Investment Company

We need a letterhead and envelope design.
We are a family owned investment company doing direct investments into other family owned businesses.
I have attached all our current marketing material including our logo for reference.

Our under construction website can be found here:
https://rob-darke-qv7m.pagevorlo.com/
password: Copperfen

Target Market(s)

Bankers, business owners, financial partners

Industry/Entity Type

Investment

Colors

Designer to choose colors to be used in the design.

Requirements
Must have
• Logo, and company information

```html
<!DOCTYPE html>
<html lang="en">
<head>
<meta charset="utf-8">
<title>Copperfen Holdings Inc — Stationery</title>
<link href="https://fonts.googleapis.com/css2?family=Cinzel:wght@500&family=Open+Sans:wght@400;600;700&display=swap" rel="stylesheet">
<style>
  :root {
    --backdrop: #f7ecc4;
    --paper: #ffffff;
    --gold: #e6ae12;
    --gold-light: #f2cf4f;
    --navy: #262a36;
    --navy-deep: #14151f;
    --rule-grey: #b9b9bd;
    --tile: #ecebe8;
    --tile-warm: #f6ecd8;
    --ink: #555860;
  }
  * { box-sizing: border-box; margin: 0; padding: 0; }
  html, body { width: 1200px; height: 900px; overflow: hidden; }
  body { background: var(--backdrop); font-family: "Open Sans", sans-serif; position: relative; }

  .piece { position: absolute; background: var(--paper); overflow: hidden; }
  .piece--dark { background: linear-gradient(180deg, #4a505c 0%, var(--navy) 40%, var(--navy-deep) 100%); }

  .wordmark {
    font-family: "Cinzel", serif; font-weight: 500; color: var(--navy);
    white-space: nowrap; line-height: 1; letter-spacing: .02em;
  }
  .piece--dark .wordmark { color: #ffffff; }

  .header { position: absolute; left: 0; right: 0; display: flex; align-items: center; }
  .header__gold { height: 5px; background: var(--gold); flex: none; }
  .header__grey { height: 4px; background: linear-gradient(180deg, #d5d5d8, #9d9da3); flex: 1; }
  .header .wordmark { margin: 0 6px; }

  .tiles { position: absolute; }
  .tiles span { position: absolute; background: var(--tile); }
  .tiles span.warm { background: var(--tile-warm); }

  .swoosh { position: absolute; left: 0; width: 100%; }

  .footer { position: absolute; left: 0; right: 0; bottom: 0; }
  .footer__contacts {
    font-size: 4.2px; color: var(--ink); white-space: nowrap; padding-left: 6px;
    display: flex; gap: 6px; align-items: center;
  }
  .footer__bar { display: flex; align-items: flex-end; margin-top: 2px; }
  .footer__bar-thin { flex: 1; height: 2px; background: var(--gold); }
  .footer__web {
    background: var(--gold); color: #fff; font-weight: 700; font-size: 5.5px;
    padding: 2px 6px; white-space: nowrap;
  }
  .dot { display: inline-block; width: 4px; height: 4px; border-radius: 50%; background: var(--gold); vertical-align: middle; margin-right: 2px; }

  /* placements */
  .sticker { height: 36px; }
  .sticker .wordmark { font-size: 6px; position: absolute; top: 15px; left: 0; right: 0; text-align: center; }

  .slip { left: 100px; top: 150px; width: 322px; height: 162px; }
  .envelope { left: 88px; top: 346px; width: 330px; height: 214px; }
  .compliments { left: 82px; top: 597px; width: 330px; height: 162px; }
  .letterhead { left: 452px; top: 88px; width: 340px; height: 470px; }
  .folder { left: 775px; top: 175px; width: 330px; height: 445px; }
  .card-front { left: 458px; top: 638px; width: 283px; height: 160px; }
  .card-back { left: 777px; top: 644px; width: 283px; height: 163px; }

  .flap { position: absolute; left: 0; top: 0; width: 100%; height: 52px; background: var(--gold-light); }
  .flap-shadow { position: absolute; left: 12px; right: 24px; top: 42px; height: 38px; background: var(--navy); clip-path: polygon(0 0, 100% 0, 97% 100%, 3% 100%); }

  .centered-mark { position: absolute; left: 0; right: 0; text-align: center; }
  .centered-mark .rule { display: block; margin: 5px auto 0; height: 1px; background: var(--gold); }

  .compliments__label { position: absolute; right: 10px; top: 36px; font-size: 6px; font-weight: 600; color: var(--gold); }

  .folder__web { position: absolute; right: 14px; bottom: 14px; color: #fff; font-weight: 700; font-size: 9.5px; }
  .card-front__web {
    position: absolute; left: 50%; bottom: 4px; transform: translateX(-50%);
    background: var(--gold); color: #fff; font-size: 6.5px; font-weight: 700;
    padding: 3px 10px 5px; border-radius: 4px 4px 0 0;
  }
  .card-front__base { position: absolute; left: 0; right: 0; bottom: 0; height: 6px; background: var(--gold); }

  .card-back__divider { position: absolute; left: 150px; top: 40px; width: 1px; height: 90px; background: #d8d8d8; }
  .card-back__details { position: absolute; left: 160px; top: 44px; color: var(--ink); font-size: 6.4px; line-height: 1.32; }
  .card-back__name { color: var(--gold); font-weight: 700; font-size: 9.5px; }
  .card-back__details .row { display: flex; gap: 4px; padding-left: 2px; }
  .card-back__base { position: absolute; left: 0; right: 0; bottom: 0; height: 5px; display: flex; gap: 2px; }
  .card-back__base span { flex: 1; background: var(--rule-grey); }
  .card-back__base span.gold { background: var(--gold); flex: 2.2; }
</style>
</head>
<body>

  <!-- Seal stickers -->
  <div class="piece sticker" style="left:225px; top:90px; width:84px;"><span class="wordmark">Copperfen Holdings</span></div>
  <div class="piece sticker" style="left:345px; top:93px; width:80px;"><span class="wordmark">Copperfen Holdings</span></div>

  <!-- DL letterhead slip -->
  <section class="piece slip">
    <div class="tiles" style="right:6px; top:10px;">
      <span style="right:20px; top:0; width:16px; height:16px;"></span>
      <span class="warm" style="right:36px; top:6px; width:16px; height:16px;"></span>
      <span class="warm" style="right:4px; top:30px; width:24px; height:22px;"></span>
    </div>
    <div class="header" style="top:40px;">
      <span class="header__gold" style="width:28px;"></span>
      <span class="wordmark" style="font-size:9px;">Copperfen Holdings Inc</span>
      <span class="header__grey"></span>
    </div>
    <svg class="swoosh" style="bottom:18px; height:60px;" viewBox="0 0 322 60" preserveAspectRatio="none">
      <path d="M0 60 C90 40 200 10 322 2 L322 14 C220 20 120 44 60 60 Z" fill="#f1f1f1"/>
      <path d="M120 60 C180 42 250 24 322 18 L322 28 C260 34 200 48 170 60 Z" fill="#f8f3e6"/>
    </svg>
    <div class="footer">
      <div class="footer__contacts"><span><i class="dot"></i>Copperfen Holdings, Inc., 48 Alder Row; Suite 210, Marlow Falls, OH 44012</span><span>555-204-7781</span><span>inquiries@copperfenholdings.com</span></div>
      <div class="footer__bar"><span class="footer__bar-thin"></span><span class="footer__web">www.copperfenholdings.com</span></div>
    </div>
  </section>

  <!-- Envelope -->
  <section class="piece envelope">
    <div class="flap-shadow"></div>
    <div class="flap"></div>
    <div class="centered-mark" style="top:182px;">
      <span class="wordmark" style="font-size:9px;">Copperfen Holdings Inc</span>
    </div>
  </section>

  <!-- Compliments slip -->
  <section class="piece compliments">
    <div class="tiles" style="right:6px; top:8px;">
      <span style="right:14px; top:0; width:18px; height:14px;"></span>
      <span class="warm" style="right:4px; top:40px; width:24px; height:22px;"></span>
    </div>
    <div class="header" style="top:40px;">
      <span class="header__gold" style="width:34px;"></span>
      <span class="wordmark" style="font-size:9px;">Copperfen Holdings Inc</span>
      <span class="header__grey"></span>
    </div>
    <span class="compliments__label">With Compliments</span>
    <svg class="swoosh" style="bottom:18px; height:60px;" viewBox="0 0 330 60" preserveAspectRatio="none">
      <path d="M0 60 C90 40 210 10 330 2 L330 14 C230 20 120 44 60 60 Z" fill="#f1f1f1"/>
      <path d="M120 60 C180 42 260 24 330 18 L330 28 C270 34 200 48 170 60 Z" fill="#f8f3e6"/>
    </svg>
    <div class="footer">
      <div class="footer__contacts"><span><i class="dot"></i>Copperfen Holdings, Inc., 48 Alder Row; Suite 210, Marlow Falls, OH 44012</span><span>555-204-7781</span><span>inquiries@copperfenholdings.com</span></div>
      <div class="footer__bar"><span class="footer__bar-thin"></span><span class="footer__web">www.copperfenholdings.com</span></div>
    </div>
  </section>

  <!-- A4 letterhead -->
  <section class="piece letterhead">
    <div class="tiles" style="right:0; top:8px;">
      <span style="right:36px; top:0; width:28px; height:22px;"></span>
      <span class="warm" style="right:64px; top:10px; width:26px; height:24px;"></span>
      <span style="right:64px; top:38px; width:26px; height:26px;"></span>
      <span class="warm" style="right:6px; top:46px; width:40px; height:38px;"></span>
    </div>
    <div class="header" style="top:50px;">
      <span class="header__gold" style="width:30px;"></span>
      <span class="wordmark" style="font-size:10px;">Copperfen Holdings Inc</span>
      <span class="header__grey"></span>
    </div>
    <svg class="swoosh" style="bottom:18px; height:90px;" viewBox="0 0 340 90" preserveAspectRatio="none">
      <path d="M0 80 C100 64 220 20 340 4 L340 20 C230 32 120 70 40 90 L0 90 Z" fill="#eeeeee"/>
      <path d="M110 90 C190 64 270 40 340 32 L340 44 C280 50 210 70 170 90 Z" fill="#f8f3e6"/>
    </svg>
    <div class="footer">
      <div class="footer__contacts"><span><i class="dot"></i>Copperfen Holdings, Inc., 48 Alder Row; Suite 210, Marlow Falls, OH 44012</span><span>555-204-7781</span><span>inquiries@copperfenholdings.com</span></div>
      <div class="footer__bar"><span class="footer__bar-thin"></span><span class="footer__web">www.copperfenholdings.com</span></div>
    </div>
  </section>

  <!-- Presentation folder -->
  <section class="piece piece--dark folder">
    <div class="tiles" style="right:0; top:6px;">
      <span style="right:28px; top:0; width:38px; height:28px; background:rgba(255,255,255,.08);"></span>
      <span style="right:66px; top:10px; width:24px; height:22px; background:rgba(255,255,255,.1);"></span>
      <span style="right:66px; top:36px; width:24px; height:24px; background:rgba(255,255,255,.1);"></span>
      <span style="right:6px; top:40px; width:38px; height:38px; background:rgba(255,255,255,.08);"></span>
    </div>
    <div class="centered-mark" style="top:240px;">
      <span class="wordmark" style="font-size:18px;">Copperfen Holdings Inc</span>
      <span class="rule" style="width:205px;"></span>
    </div>
    <svg class="swoosh" style="bottom:0; height:100px;" viewBox="0 0 330 100" preserveAspectRatio="none">
      <path d="M0 60 C110 30 230 20 330 10 L330 24 C230 34 110 50 0 80 Z" fill="rgba(255,255,255,.05)"/>
      <path d="M0 85 C120 55 240 40 330 34 L330 44 C240 52 120 72 0 100 Z" fill="rgba(0,0,0,.3)"/>
    </svg>
    <span class="folder__web">www.copperfenholdings.com</span>
  </section>

  <!-- Business card, front -->
  <section class="piece piece--dark card-front">
    <div class="centered-mark" style="top:80px;">
      <span class="wordmark" style="font-size:14.5px;">Copperfen Holdings Inc</span>
      <span class="rule" style="width:180px;"></span>
    </div>
    <span class="card-front__base"></span>
    <span class="card-front__web">www.copperfenholdings.com</span>
  </section>

  <!-- Business card, back -->
  <section class="piece card-back">
    <span class="wordmark" style="position:absolute; left:10px; top:78px; font-size:8.6px;">Copperfen Holdings Inc</span>
    <span class="card-back__divider"></span>
    <div class="card-back__details">
      <div class="card-back__name">Nora Vale</div>
      <div>Vice President</div>
      <div class="row"><i class="dot"></i><span>Copperfen Holdings, Inc.<br>48 Alder Row; Suite 210<br>Marlow Falls, OH 44012</span></div>
      <div class="row"><i class="dot"></i><span>555-204-7781</span></div>
      <div class="row"><i class="dot"></i><span>inquiries@copperfenholdings.com</span></div>
      <div class="row"><i class="dot"></i><span>www.copperfenholdings.com</span></div>
    </div>
    <div class="card-back__base"><span></span><span></span><span></span><span class="gold"></span></div>
  </section>

</body>
</html>
```